Stage Design Company Business Card

We are looking to step up up our business card design for our team.

We are a Full service Design and Consultation company for Stage and TV with an emphasis in Theatrical Lighting.

We like our materials to be clean and modern with solid colors free of patterns and gradients. Our brand consists of 4 primary colors Purple, Black, Grey, and White. Provided is our Word Mark as well as our Symbol Logo.

We would like our cards to leave an impression beyond the information, show our attention to design and detail, and make our marks an easily recognized feature (together or apart) for our clients.

We need a warm approachable comfortable feel for some clients, and a professional flair for the board member type clients.

Attached are our brand elements, and our existing cards to give a sense of our style and a glipse at the information we provide on our cards.

Target Market(s)

broad client base from church leaders to high school teachers and architects.

Industry/Entity Type

Business

Contact Information for Business Card

We format our phone number with periods not parenthesis or dashes. Information will be edited for each of our team members, and team member specific cards are not part of this scope, but rather a template so to speak.

Font styles to use
Sans Serif

Colors
6b449b
ffffff
000000
333333
aaaaaa

Requirements
Must have
• Wordmark and logo mark present (does not need to exist on the same side of card)
• Brand Colors,
• Name, Phone, Email, Address.
• Unique choices that make someone stop and take a second look
Nice to have
• It would be nice to somehow convey what we DO, as our brand name does not lend itself to this, outside of an obvious tagline though.....
• social media if not crowded. all of our handles match (instagram, twitter, facebook)
Should not have
• "clipart"

```html
<!DOCTYPE html>
<html lang="en">
<head>
<meta charset="utf-8">
<title>Marlow Stagecraft – Business Card</title>
<link rel="stylesheet" href="https://fonts.googleapis.com/css2?family=Roboto+Condensed:wght@400;700&family=Montserrat:wght@500&display=swap">
<style>
  :root {
    --brand-purple: #6b3ff2;
    --mark-lilac: #b9a4ff;
    --card-grey: #cccccc;
    --ink: #111111;
    --paper-white: #ffffff;
    --backdrop: #000000;
  }
  html, body {
    margin: 0;
    padding: 0;
    width: 1200px;
    height: 1200px;
    overflow: hidden;
    background: var(--backdrop);
  }
  .canvas {
    position: relative;
    width: 1200px;
    height: 1200px;
  }
  .card {
    position: absolute;
    left: 180px;
    width: 840px;
    height: 480px;
    overflow: hidden;
  }

  /* Front side */
  .card-front {
    top: 80px;
    background: var(--brand-purple);
  }
  .front-mark {
    position: absolute;
    left: 50%;
    top: 48px;
    width: 190px;
    height: 190px;
    margin-left: -95px;
    border-radius: 50%;
    background: var(--mark-lilac);
  }
  .front-name {
    position: absolute;
    left: 0;
    right: 0;
    top: 292px;
    text-align: center;
    font-family: "Montserrat", sans-serif;
    font-weight: 500;
    font-size: 40px;
    letter-spacing: 0.32em;
    padding-left: 0.32em;
    color: var(--paper-white);
  }
  .front-rule {
    position: absolute;
    left: 210px;
    right: 150px;
    top: 380px;
    border-top: 2px dashed var(--paper-white);
    opacity: 0.85;
  }

  /* Back side */
  .card-back {
    top: 640px;
    background: var(--card-grey);
  }
  .back-band-top,
  .back-band-bottom {
    position: absolute;
    left: 0;
    right: 0;
    background: var(--brand-purple);
  }
  .back-band-top { top: 0; height: 46px; }
  .back-band-bottom { bottom: 0; height: 36px; }

  .contact {
    position: absolute;
    left: 340px;
    width: 400px;
    top: 258px;
    text-align: center;
    font-family: "Roboto Condensed", sans-serif;
    color: var(--ink);
    font-size: 26px;
    line-height: 1.32;
  }
  .contact p { margin: 0; }
  .contact-name {
    font-weight: 700;
    font-size: 28px;
  }
</style>
</head>
<body>
<main class="canvas">
  <section class="card card-front" aria-label="Card front">
    <div class="front-mark" role="img" aria-label="Company symbol"></div>
    <div class="front-name">MARLOW STAGECRAFT</div>
    <div class="front-rule"></div>
  </section>

  <section class="card card-back" aria-label="Card back">
    <div class="back-band-top"></div>
    <div class="contact">
      <p class="contact-name">Owen R Tanner</p>
      <p class="contact-address">52 E Cedar Ave Tempe, AZ 85281</p>
      <p class="contact-web">marlow-s.com</p>
      <p class="contact-phone">800.555.0142</p>
    </div>
    <div class="back-band-bottom"></div>
  </section>
</main>
</body>
</html>
```